Payment button (Check out) design

We need a logo design for a payment check out for an online retail store, www.trelvix.com. This payment check button should represent customer can check out via credit card and debit card, other than frobex check out.

Target Market(s)

UK

Industry/Entity Type

Digital Camera

Logo Text

Pay with credit/debit card (prefer in blue tone, consistent with our logo design)

Logo styles of interest
Wordmark Logo
Font styles to use
Serif
Sans Serif

Colors
0355a3
3176b5
85acd3
85cae6
33a6d7
0692cd

```html
<!DOCTYPE html>
<html lang="en">
<head>
<meta charset="utf-8">
<title>Pay with Credit/Debit Card — button options</title>
<link rel="stylesheet" href="https://fonts.googleapis.com/css2?family=Source+Sans+3:ital,wght@1,600;1,700&family=Roboto:wght@400&display=swap">
<style>
  :root {
    --canvas-light: #fdfdfd;
    --canvas-grey: #f1f1f1;
    --label-grey: #c6c6c6;
    --btn-top: #4fa7e0;
    --btn-mid: #1277bd;
    --btn-bottom: #10579c;
    --btn-edge: #1a6fb6;
    --gloss-top: #8fd1f4;
    --ink-white: #ffffff;
    --card-navy: #0b3f74;
    --card-edge: #2a6aa8;
  }
  html, body {
    margin: 0;
    padding: 0;
    width: 1200px;
    height: 1200px;
    overflow: hidden;
  }
  .sheet {
    position: relative;
    width: 1200px;
    height: 1200px;
  }
  .option {
    position: absolute;
    left: 0;
    width: 1200px;
    height: 600px;
  }
  .option--light { top: 0; background: var(--canvas-light); }
  .option--grey { top: 600px; background: var(--canvas-grey); }
  .option-number {
    position: absolute;
    left: 46px;
    margin: 0;
    font-family: "Roboto", Arial, sans-serif;
    font-size: 34px;
    font-weight: 400;
    color: var(--label-grey);
    line-height: 1;
  }
  .pay-button {
    position: absolute;
    display: block;
    overflow: visible;
  }
  .btn-text {
    font-family: "Source Sans 3", "Myriad Pro", sans-serif;
    font-style: italic;
    fill: var(--ink-white);
  }
  .btn-text--lead { font-weight: 600; }
  .btn-text--main { font-weight: 700; }
  .card-digits {
    font-family: "Roboto", Arial, sans-serif;
    font-size: 3px;
    fill: var(--ink-white);
  }
</style>
</head>
<body>
<main class="sheet">
  <svg width="0" height="0" aria-hidden="true" style="position:absolute">
    <defs>
      <linearGradient id="btnFill" x1="0" y1="0" x2="0" y2="1">
        <stop offset="0" stop-color="var(--btn-top)"/>
        <stop offset="0.5" stop-color="var(--btn-mid)"/>
        <stop offset="1" stop-color="var(--btn-bottom)"/>
      </linearGradient>
      <linearGradient id="btnGloss" x1="0" y1="0" x2="0" y2="1">
        <stop offset="0" stop-color="var(--gloss-top)" stop-opacity="0.95"/>
        <stop offset="1" stop-color="#4fa2dc" stop-opacity="0.35"/>
      </linearGradient>
      <filter id="btnShadow" x="-5%" y="-20%" width="112%" height="150%">
        <feDropShadow dx="5" dy="6" stdDeviation="3" flood-color="#000" flood-opacity="0.28"/>
      </filter>
    </defs>
  </svg>

  <section class="option option--light">
    <p class="option-number" style="top:279px">01</p>
    <svg class="pay-button" style="left:367px; top:254px" width="466" height="92" viewBox="0 0 466 92" role="img" aria-label="Pay with Credit/Debit Card">
      <rect x="1" y="1" width="464" height="90" rx="45" fill="url(#btnFill)" stroke="var(--btn-edge)" stroke-width="2" filter="url(#btnShadow)"/>
      <rect x="16" y="4" width="434" height="42" rx="21" fill="url(#btnGloss)"/>
      <text class="btn-text btn-text--lead" x="49" y="57" font-size="35">Pay with</text>
      <text class="btn-text btn-text--main" x="203" y="42" font-size="42">Credit/</text>
      <text class="btn-text btn-text--main" x="202" y="80" font-size="42">Debit Card</text>
      <g class="card-icon" transform="translate(346 12)">
        <rect x="0" y="0" width="48" height="30" rx="2.5" fill="var(--card-navy)" stroke="var(--card-edge)" stroke-width="0.8"/>
        <rect x="5" y="4" width="6" height="6" fill="#ffffff" opacity="0.9"/>
        <ellipse cx="37" cy="8" rx="6" ry="4" fill="#ffffff"/>
        <text class="card-digits" x="6" y="24">0000 0000 0000 0000</text>
      </g>
    </svg>
  </section>

  <section class="option option--grey">
    <p class="option-number" style="top:285px">02</p>
    <svg class="pay-button" style="left:276px; top:253px" width="648" height="92" viewBox="0 0 648 92" role="img" aria-label="Pay with Credit/Debit Card">
      <rect x="1" y="1" width="646" height="90" rx="45" fill="url(#btnFill)" stroke="var(--btn-edge)" stroke-width="2" filter="url(#btnShadow)"/>
      <rect x="16" y="4" width="616" height="42" rx="21" fill="url(#btnGloss)"/>
      <text class="btn-text btn-text--lead" x="36" y="59" font-size="35">Pay with</text>
      <text class="btn-text btn-text--main" x="174" y="65" font-size="57">Credit/Debit Card</text>
    </svg>
  </section>
</main>
</body>
</html>
```